Alloy wheel repair business needs a website

Install logo previously purchased from pixelbazaar, toolbar with dropdowns. services, gallery, clients , contact ect
Maybe mission statment

Target Market(s)

vehicle owners, auto dealers,insurance companies,

Industry/Entity Type

Alloy Wheel Repair

Coding

Coded - Design and coding required

Number of Pages Required

4 page

Font styles to use
Sans Serif

Colors
0054AA
0677BA
7BADD7
CADEEF
E8F1F8

```html
<!DOCTYPE html>
<html lang="en">
<head>
<meta charset="utf-8">
<title>Spokeline Repair – Alloy Wheel Services</title>
<link href="https://fonts.googleapis.com/css2?family=Orbitron:wght@800;900&family=Montserrat:wght@400;500;600;700&display=swap" rel="stylesheet">
<style>
:root{
  --blue:#0054AA;
  --blue-2:#0677BA;
  --blue-3:#7BADD7;
  --blue-4:#CADEEF;
  --blue-5:#E8F1F8;
  --dark:#1d191c;
  --ink:#1b1b1b;
  --muted:#5b5b5b;
  --star:#f5b301;
  --white:#fff;
}
*{box-sizing:border-box;margin:0;padding:0}
html,body{width:1200px;height:4556px;overflow:hidden}
body{position:relative;font-family:"Montserrat",sans-serif;color:var(--ink);background:var(--white)}
.abs{position:absolute}
.display{font-family:"Orbitron",sans-serif;font-weight:900;text-transform:uppercase;letter-spacing:2px}
.section-title{position:absolute;left:0;width:1200px;text-align:center;font-size:34px;color:var(--blue)}
.section-title::after{content:"";display:block;width:80px;height:3px;background:#222;margin:6px auto 0}
.dark .section-title::after{background:#3a3a3a}

/* header */
.site-header{position:absolute;top:0;left:0;width:1200px;height:88px;background:var(--white);box-shadow:0 1px 4px rgba(0,0,0,.08);z-index:5}
.brand{position:absolute;left:88px;top:30px;font-family:"Montserrat",sans-serif;font-weight:700;color:var(--blue);font-size:22px;line-height:28px;white-space:nowrap}
.nav{position:absolute;left:510px;top:34px;display:flex;font-size:15px}
.nav a{color:#222;text-decoration:none;margin-right:30px;position:relative}
.nav a.active{color:var(--blue)}
.nav a.active::after{content:"";position:absolute;left:-4px;right:-4px;top:44px;height:3px;background:var(--blue)}
.head-icon{position:absolute;top:27px;width:32px;height:32px;display:flex;align-items:center;justify-content:center}
.head-icon.phone{left:1037px;background:var(--blue)}
.head-icon.mail{left:1080px;border:1.5px solid #222}

/* hero */
.hero-photo{position:absolute;top:88px;left:0;width:1200px;height:567px;background:linear-gradient(120deg,#3c3c40 0%,#1c1c1f 45%,#4a4a4f 75%,#232326 100%)}
.hero-title{position:absolute;top:235px;left:0;width:1200px;text-align:center;color:#fff;font-size:50px;line-height:62px;letter-spacing:4px}
.btn{position:absolute;display:flex;align-items:center;justify-content:center;font-size:15px;font-weight:600}
.btn-blue{background:var(--blue);color:#fff}
.btn-line{border:1.5px solid #333;color:#222;background:#fff}

/* about */
.about-title{position:absolute;left:88px;top:735px;font-size:34px;color:var(--blue)}
.about-title::after{content:"";display:block;width:150px;height:3px;background:#222;margin-top:2px}
.about-text{position:absolute;left:88px;top:810px;width:495px;font-size:13.5px;line-height:21px;color:#333}
.about-text p{margin-bottom:17px}
.about-text .lead{font-weight:700;font-size:14.5px;color:#111}
.about-frame{position:absolute;left:650px;top:744px;width:440px;height:345px;background:var(--blue)}
.about-photo{position:absolute;left:658px;top:708px;width:454px;height:372px;background:linear-gradient(135deg,#7b7b7e,#2b2b2e 60%,#55575b)}

/* services */
.service-card{position:absolute;top:1405px;width:187px;height:224px;border:1px solid #3a3639;color:#bdbdbd;text-align:center;font-size:16px;line-height:19px}
.service-card svg{display:block;margin:38px auto 26px}
.service-card.active{background:var(--blue);border-color:var(--blue);color:#fff}

/* gallery */
.gallery-item{position:absolute;width:320px;height:197px;display:flex}
.gallery-item div{flex:1;position:relative}
.gallery-item div+div{border-left:1px solid rgba(255,255,255,.5)}
.gallery-item span{position:absolute;bottom:4px;left:0;right:0;text-align:center;color:rgba(255,255,255,.75);font-size:16px}

/* blogs */
.blog{position:absolute;top:2736px;width:320px}
.blog-photo{height:215px;background:linear-gradient(135deg,#5e5e63,#24242a 60%,#3e4147)}
.blog-date{position:absolute;left:16px;top:160px;width:80px;height:78px;background:var(--blue);color:#fff;font-size:13px;padding:14px 0 0 17px;line-height:17px}
.blog h3{margin-top:40px;padding-left:16px;color:var(--blue);font-size:14.5px;font-weight:500}
.blog p{padding-left:16px;color:#cfcfcf;font-size:13.5px;line-height:20px;margin-top:10px;width:300px}
.blog a{display:block;padding-left:16px;margin-top:12px;color:#cfcfcf;font-size:13px;text-decoration:underline}

/* testimonials */
.tabs{position:absolute;left:241px;top:3472px;width:717px;height:41px;display:flex;border:1px solid #cfcfcf}
.tab{flex:1;display:flex;align-items:center;justify-content:center;gap:8px;font-size:14px;border-right:1px solid #cfcfcf}
.tab:last-child{border-right:0}
.tab.active{background:var(--blue);color:#fff;position:relative}
.tab.active::after{content:"";position:absolute;bottom:-8px;left:50%;margin-left:-8px;border:8px solid transparent;border-bottom:0;border-top-color:var(--blue)}
.dot{width:16px;height:16px;border-radius:50%}
.review{position:absolute;width:320px;height:214px;background:#fff;box-shadow:0 2px 14px rgba(0,0,0,.1);padding:22px 20px}
.avatar{position:absolute;left:20px;top:22px;width:54px;height:54px;border-radius:50%;background:linear-gradient(135deg,#c8b7a8,#6f5a4e);border:2px solid #ddd}
.avatar.letter{display:flex;align-items:center;justify-content:center;color:#fff;font-size:22px;font-weight:500;background:var(--blue)}
.avatar.letter.green{background:#6aa84f}
.rev-name{position:absolute;left:86px;top:30px;color:var(--blue);font-size:13px;font-weight:600}
.rev-date{position:absolute;left:86px;top:48px;color:#777;font-size:11.5px}
.stars{position:absolute;right:20px;top:28px;color:var(--star);font-size:16px;letter-spacing:3px}
.rev-text{position:absolute;left:20px;top:94px;width:285px;font-size:13px;line-height:19px;color:#444}
.rev-text u{color:#222}
.rev-source{position:absolute;left:20px;top:170px;font-size:18px;font-weight:600;color:var(--blue)}

/* footer */
.site-footer{position:absolute;left:0;top:4190px;width:1200px;height:366px;background:var(--dark);color:#fff}
.foot-brand{position:absolute;left:88px;top:68px;font-weight:700;font-size:22px;line-height:28px;white-space:nowrap}
.socials{position:absolute;left:88px;top:130px;display:flex;gap:12px}
.socials span{width:30px;height:30px;border-radius:50%;border:1px solid #666}
.socials span.on{background:var(--blue);border-color:var(--blue)}
.foot-head{position:absolute;top:60px;color:var(--blue-2);font-size:15px;font-weight:500;letter-spacing:1px;text-transform:uppercase;line-height:18px}
.contact-row{position:absolute;left:326px;display:flex;gap:12px;font-size:13.5px;line-height:19px}
.contact-row em{display:block;font-style:normal;color:var(--blue-2)}
.links{position:absolute;left:591px;top:98px;font-size:13.5px;line-height:24px}
.links a{display:block;color:#fff;text-decoration:none}
.links a.active{color:var(--blue-2);text-decoration:underline}
.news-text{position:absolute;left:783px;top:102px;width:320px;font-size:13.5px;line-height:16px}
.news-input{position:absolute;left:783px;top:155px;width:328px;height:38px;background:#fff;color:#888;font-size:12.5px;padding:12px 20px}
.news-btn{position:absolute;left:783px;top:211px;width:122px;height:36px;border:1.5px solid var(--blue);color:var(--blue-2);font-size:13px;display:flex;align-items:center;justify-content:center}
.foot-rule{position:absolute;left:0;top:308px;width:1200px;height:1px;background:#333}
.copy{position:absolute;left:0;top:328px;width:1200px;text-align:center;font-size:12px}
</style>
</head>
<body>

<header class="site-header">
  <div class="brand">Spokeline Repair</div>
  <nav class="nav">
    <a class="active">Home</a><a>About</a><a>Services</a><a>Gallery</a><a>Blogs</a><a>Contact Us</a>
  </nav>
  <div class="head-icon phone"><svg width="16" height="16" viewBox="0 0 24 24" fill="#fff"><path d="M6.6 10.8a15 15 0 006.6 6.6l2.2-2.2c.3-.3.7-.4 1-.2 1.1.4 2.3.6 3.6.6.6 0 1 .4 1 1V20c0 .6-.4 1-1 1A17 17 0 013 4c0-.6.4-1 1-1h3.5c.6 0 1 .4 1 1 0 1.3.2 2.5.6 3.6.1.3 0 .7-.2 1z"/></svg></div>
  <div class="head-icon mail"><svg width="16" height="12" viewBox="0 0 24 18" fill="#222"><path d="M0 0h24v18H0z"/><path d="M2 2l10 7 10-7" fill="none" stroke="#fff" stroke-width="2"/></svg></div>
</header>

<!-- hero -->
<div class="hero-photo" role="img" aria-label="Mechanic fitting an alloy wheel in a workshop"></div>
<svg class="abs" style="top:0;left:0" width="1200" height="700">
  <polygon points="0,655 1200,545 1200,700 0,700" fill="#fff"/>
  <polygon points="690,570 1200,520 1200,622" fill="var(--blue)"/>
</svg>
<h1 class="hero-title display">Alloy Wheel<br>Services</h1>
<div class="btn btn-blue" style="left:510px;top:388px;width:168px;height:40px">Appointment</div>

<!-- about -->
<h2 class="about-title display">About Us</h2>
<div class="about-text">
  <p class="lead">Lorem Ipsum is simply dummy text of the printing and typesetting industry.</p>
  <p>Lorem Ipsum has been the industry's standard dummy text ever since the 1500s, when an unknown printer took a galley of type and scrambled it to make a type specimen book.</p>
  <p>It has survived not only five centuries, but also the leap into electronic typesetting, remaining essentially unchanged.</p>
</div>
<div class="btn btn-line" style="left:88px;top:1035px;width:146px;height:38px">Read More</div>
<div class="about-frame"></div>
<div class="about-photo" role="img" aria-label="Technician carrying a tyre"></div>

<!-- services -->
<section class="dark">
  <svg class="abs" style="top:1165px;left:0" width="1200" height="625">
    <polygon points="0,80 1200,5 1200,625 0,625" fill="var(--dark)"/>
    <polygon points="0,8 440,57 0,88" fill="var(--blue)"/>
    <polygon points="690,575 1200,545 1200,625" fill="var(--blue)"/>
  </svg>
  <h2 class="section-title display" style="top:1310px">Services</h2>
  <div class="service-card" style="left:88px">
    <svg width="92" height="92" viewBox="0 0 92 92"><circle cx="46" cy="46" r="44" fill="#888"/><circle cx="46" cy="46" r="30" fill="none" stroke="#1d191c" stroke-width="5"/><circle cx="46" cy="46" r="10" fill="#1d191c"/></svg>Wheel Repair<br>Services</div>
  <div class="service-card" style="left:297px">
    <svg width="92" height="92" viewBox="0 0 92 92" fill="#888"><rect x="30" y="10" width="18" height="26"/><rect x="20" y="36" width="40" height="18"/><rect x="32" y="54" width="14" height="30"/><circle cx="70" cy="40" r="3"/><circle cx="80" cy="46" r="3"/><circle cx="70" cy="52" r="3"/></svg>Wheel Custom<br>Coloring</div>
  <div class="service-card" style="left:506px">
    <svg width="92" height="92" viewBox="0 0 92 92"><circle cx="46" cy="46" r="44" fill="#888"/><circle cx="46" cy="46" r="28" fill="#1d191c"/><circle cx="46" cy="46" r="9" fill="#888"/><g fill="#888"><circle cx="46" cy="28" r="6"/><circle cx="63" cy="52" r="6"/><circle cx="29" cy="52" r="6"/></g></svg>Wheel<br>Refinishing</div>
  <div class="service-card active" style="left:716px">
    <svg width="92" height="92" viewBox="0 0 92 92"><circle cx="40" cy="46" r="34" fill="none" stroke="#fff" stroke-width="8"/><circle cx="40" cy="46" r="10" fill="#fff"/><rect x="66" y="14" width="12" height="64" rx="6" fill="#fff"/></svg>Wheel<br>Straightening</div>
  <div class="service-card" style="left:925px">
    <svg width="92" height="92" viewBox="0 0 92 92"><circle cx="40" cy="46" r="34" fill="none" stroke="#888" stroke-width="9" stroke-dasharray="10 4"/><circle cx="40" cy="46" r="12" fill="#888"/><rect x="74" y="20" width="9" height="56" fill="#888"/></svg>Wheel<br>Remanufacturing</div>
</section>

<!-- gallery -->
<h2 class="section-title display" style="top:1840px">Gallery</h2>
<div class="gallery-item" style="left:88px;top:1925px"><div role="img" aria-label="Gold five-spoke wheel before repair" style="background:linear-gradient(135deg,#8a8270,#2e2c28)"><span>Before</span></div><div role="img" aria-label="Gold five-spoke wheel after repair" style="background:linear-gradient(135deg,#a39774,#2e2c28)"><span>After</span></div></div>
<div class="gallery-item" style="left:440px;top:1925px"><div role="img" aria-label="Black wheel before repair" style="background:linear-gradient(135deg,#5d5d60,#1c1c1e)"><span>Before</span></div><div role="img" aria-label="Black wheel after repair" style="background:linear-gradient(135deg,#6a6a6e,#1a1a1c)"><span>After</span></div></div>
<div class="gallery-item" style="left:792px;top:1925px"><div role="img" aria-label="Tyre and wheel before service" style="background:linear-gradient(135deg,#6e7169,#2b2c2a)"><span>Before</span></div><div role="img" aria-label="Tyre and wheel after service" style="background:linear-gradient(135deg,#7a7d76,#2b2c2a)"><span>After</span></div></div>
<div class="gallery-item" style="left:88px;top:2154px"><div role="img" aria-label="Silver car wheel before repair" style="background:linear-gradient(135deg,#c9cacb,#55585c)"><span>Before</span></div><div role="img" aria-label="Silver car wheel after repair" style="background:linear-gradient(135deg,#d3d4d5,#5b5e61)"><span>After</span></div></div>
<div class="gallery-item" style="left:440px;top:2154px"><div role="img" aria-label="White car wheel before repair" style="background:linear-gradient(135deg,#bfc0c2,#4a4c50)"><span>Before</span></div><div role="img" aria-label="White car wheel after repair" style="background:linear-gradient(135deg,#d8d8d9,#6d6f72)"><span>After</span></div></div>
<div class="gallery-item" style="left:792px;top:2154px"><div role="img" aria-label="Gold wheel before refinishing" style="background:linear-gradient(135deg,#8a8270,#2e2c28)"><span>Before</span></div><div role="img" aria-label="Gold wheel after refinishing" style="background:linear-gradient(135deg,#a39774,#2e2c28)"><span>After</span></div></div>
<div class="btn btn-blue" style="left:537px;top:2393px;width:126px;height:39px">View All</div>

<!-- blogs -->
<section class="dark">
  <svg class="abs" style="top:2505px;left:0" width="1200" height="795">
    <polygon points="0,90 1200,5 1200,705 0,795" fill="var(--dark)"/>
    <polygon points="0,10 440,58 0,92" fill="var(--blue)"/>
    <polygon points="690,745 1200,705 1200,795" fill="var(--blue)"/>
  </svg>
  <h2 class="section-title display" style="top:2650px">Blogs</h2>
  <article class="blog" style="left:88px"><div class="blog-photo" role="img" aria-label="Mechanic inspecting a brake disc"></div><div class="blog-date">▦<br>Sep 04<br>2023</div><h3>Lorem Ipsum is simply dummy text</h3><p>Lorem Ipsum is simply dummy text of the printing and typesetting industry.</p><a>Read More</a></article>
  <article class="blog" style="left:440px"><div class="blog-photo" role="img" aria-label="Technician rolling a tyre in a garage"></div><div class="blog-date">▦<br>Sep 04<br>2023</div><h3>Lorem Ipsum is simply dummy text</h3><p>Lorem Ipsum is simply dummy text of the printing and typesetting industry.</p><a>Read More</a></article>
  <article class="blog" style="left:792px"><div class="blog-photo" role="img" aria-label="Mechanic balancing a wheel"></div><div class="blog-date">▦<br>Sep 04<br>2023</div><h3>Lorem Ipsum is simply dummy text</h3><p>Lorem Ipsum is simply dummy text of the printing and typesetting industry.</p><a style="color:var(--blue)">Read More</a></article>
  <div class="btn" style="left:537px;top:3137px;width:126px;height:38px;border:1px solid #3a3639;color:#4a4649;font-weight:500">View All</div>
</section>

<!-- testimonials -->
<h2 class="section-title display" style="top:3385px">Testimonials</h2>
<div class="tabs">
  <div class="tab active"><b>4.5</b> All Reviews</div>
  <div class="tab"><span class="dot" style="background:var(--blue-3)"></span><b>4.2</b> Searchly</div>
  <div class="tab"><span class="dot" style="background:var(--blue-2)"></span><b>4.2</b> Friendbook</div>
  <div class="tab"><svg width="18" height="16" viewBox="0 0 18 16" fill="#222"><circle cx="9" cy="4" r="3.5"/><path d="M2 16c0-4 3-6 7-6s7 2 7 6z"/></svg>Write a review</div>
</div>

<div class="review" style="left:88px;top:3552px"><div class="avatar" role="img" aria-label="Reviewer photo"></div><div class="rev-name">Owen Talbrook</div><div class="rev-date">11 days ago</div><div class="stars">★★★★★</div><p class="rev-text">Lorem Ipsum is simply dummy text of the printing and typesetting industry. Lorem Ipsum has been the industry's standard dummy text ever... <u>Read More</u></p><div class="rev-source">Searchly</div></div>
<div class="review" style="left:440px;top:3552px"><div class="avatar" role="img" aria-label="Reviewer photo"></div><div class="rev-name">Marco Delvane</div><div class="rev-date">12 days ago</div><div class="stars">★★★★★</div><p class="rev-text">Lorem Ipsum is simply dummy text of the printing and typesetting industry. Lorem Ipsum has been the industry's standard dummy text ever... <u>Read More</u></p><div class="rev-source">Friendbook</div></div>
<div class="review" style="left:792px;top:3552px"><div class="avatar letter">A</div><div class="rev-name">A Whitcombe</div><div class="rev-date">15 days ago</div><div class="stars">★★★★★</div><p class="rev-text">Lorem Ipsum is simply dummy text of the printing and typesetting industry. Lorem Ipsum has been the industry's standard dummy text ever... <u>Read More</u></p><div class="rev-source">Searchly</div></div>
<div class="review" style="left:88px;top:3798px"><div class="avatar" role="img" aria-label="Reviewer photo"></div><div class="rev-name">Nadia Okoro</div><div class="rev-date">August 13</div><div class="stars">★★★★★</div><p class="rev-text">Lorem Ipsum is simply dummy text of the printing and typesetting industry. Lorem Ipsum has been the industry's standard dummy text ever... <u>Read More</u></p><div class="rev-source">Searchly</div></div>
<div class="review" style="left:440px;top:3798px"><div class="avatar letter green">M</div><div class="rev-name">fernbridge</div><div class="rev-date">30 days ago</div><div class="stars">★★★★★</div><p class="rev-text">Lorem Ipsum is simply dummy text of the printing and typesetting industry. Lorem Ipsum has been the industry's standard dummy text ever... <u>Read More</u></p><div class="rev-source">Searchly</div></div>
<div class="review" style="left:792px;top:3798px"><div class="avatar" role="img" aria-label="Reviewer photo"></div><div class="rev-name">Marco Delvane</div><div class="rev-date">12 days ago</div><div class="stars">★★★★★</div><p class="rev-text">Lorem Ipsum is simply dummy text of the printing and typesetting industry. Lorem Ipsum has been the industry's standard dummy text ever... <u>Read More</u></p><div class="rev-source">Friendbook</div></div>
<div class="btn btn-line" style="left:537px;top:4055px;width:145px;height:38px">Load More</div>

<!-- footer -->
<footer class="site-footer">
  <div class="foot-brand">Spokeline Repair</div>
  <div class="socials"><span></span><span class="on"></span><span></span><span></span></div>

  <div class="foot-head" style="left:326px">Contact Info</div>
  <div class="contact-row" style="top:98px"><svg width="24" height="24" viewBox="0 0 24 24" fill="none" stroke="var(--blue-2)" stroke-width="1.5"><path d="M6.6 10.8a15 15 0 006.6 6.6l2.2-2.2 4 1.5V20A17 17 0 013 4h3.8l1.4 4z"/></svg><div><em>Call</em>555-014-2231</div></div>
  <div class="contact-row" style="top:150px"><svg width="24" height="24" viewBox="0 0 24 24" fill="none" stroke="var(--blue-2)" stroke-width="1.5"><path d="M12 22s7-7 7-12a7 7 0 00-14 0c0 5 7 12 7 12z"/><circle cx="12" cy="10" r="2.5"/></svg><div><em>Address</em>42 Foundry Lane<br>Milltown PA 10001</div></div>
  <div class="contact-row" style="top:222px"><svg width="24" height="24" viewBox="0 0 24 24" fill="none" stroke="var(--blue-2)" stroke-width="1.5"><rect x="2" y="5" width="20" height="14"/><path d="M2 5l10 8 10-8"/></svg><div><em>Email</em>hello@spokelinerepair.com</div></div>

  <div class="foot-head" style="left:591px">Quick Links</div>
  <div class="links"><a class="active">Home</a><a>About</a><a>Services</a><a>Gallery</a><a>Testimonials</a><a>Blogs</a><a>Contact Us</a></div>

  <div class="foot-head" style="left:783px;width:330px">Get latest offers and updates from Spokeline Repair!</div>
  <p class="news-text">Lorem Ipsum is dummy text of the printing industry.</p>
  <div class="news-input">Enter Your Email...</div>
  <div class="news-btn">Submit</div>

  <div class="foot-rule"></div>
  <p class="copy">© 2023 Spokeline Repair. All Right Reserved</p>
  <svg class="abs" style="left:1140px;top:322px" width="18" height="22" viewBox="0 0 18 22"><polygon points="9,0 18,22 9,16 0,22" fill="var(--blue)"/></svg>
</footer>

</body>
</html>
```